Lantern Petro - needs a business card

Lantern Petro is a U.S. based diesel sourcing and distribution company that supports American oil & gas fields through providing quality product and consistent services.

Target Market(s)

Oil and Gas

Contact Information for Business Card

The background of the card must be white to ensure the logo pops.

Font styles to use
Serif
Sans Serif

Colors

Designer to choose colors to be used in the design.

Requirements
Must have
• Front of Card: Tag line: Lantern Petro, Powering the Nation's Oil & Gas fields.
• Not sure if you guys do this part but just in case...
• Dale Winterholt
• Owner/CEO
• C:701.555.0148
• E:Dwinterholt@lanternpetro.com
• W:Lanternpetro.com
• Locations: Servicing the Powder River, DJ basin and Bakken formations.
• Back of Card: " Frac fueling is what we do. We understand how important diesel fuel is to your operation, which is why our main service line is Frac fueling. We assure our supply and stand by our service"

```html
<!DOCTYPE html>
<html lang="en">
<head>
<meta charset="utf-8">
<title>Lantern Petro – Business Card</title>
<link rel="stylesheet" href="https://fonts.googleapis.com/css2?family=Open+Sans:wght@400;600;700;800&display=swap">
<style>
  :root {
    --navy: #1c3a6e;
    --red: #b8121b;
    --grey: #4a4d52;
    --paper: #ffffff;
    --backdrop: #e6e7ea;
    --band-text: #ffffff;
  }
  * { box-sizing: border-box; margin: 0; padding: 0; }
  html, body {
    width: 1200px; height: 892px; overflow: hidden;
    background: var(--backdrop);
    font-family: "Open Sans", Arial, sans-serif;
  }
  .canvas { position: relative; width: 1200px; height: 892px; }

  .card {
    position: absolute;
    width: 580px; height: 331px;
    background: var(--paper);
    box-shadow: 0 6px 18px rgba(0,0,0,0.18);
    overflow: hidden;
  }

  /* Front card */
  .card--front { left: 60px; top: 80px; }
  .front__brand {
    position: absolute; left: 0; right: 0; top: 0; height: 190px;
    display: flex; align-items: center; justify-content: center; gap: 14px;
  }
  .brand-dot {
    width: 40px; height: 40px; border-radius: 50%;
    background: var(--navy);
  }
  .brand-name {
    color: var(--navy);
    font-weight: 800;
    font-size: 36px;
    letter-spacing: 1px;
    text-transform: uppercase;
  }
  .front__band {
    position: absolute; left: 0; right: 0; bottom: 0; height: 141px;
    background: var(--navy);
    color: var(--band-text);
    padding: 22px 28px 0;
    text-align: center;
  }
  .tagline {
    display: flex; align-items: center; gap: 12px;
    font-weight: 700; font-size: 17px;
    white-space: nowrap;
  }
  .tagline::before, .tagline::after {
    content: ""; flex: 1; height: 1px; background: var(--band-text);
  }
  .service-note {
    margin-top: 12px;
    font-size: 11.5px; line-height: 1.55;
  }

  /* Contact card */
  .card--contact { left: 560px; top: 480px; }
  .contact__mark {
    position: absolute; left: 38px; top: 72px;
    width: 220px; height: 220px; border-radius: 50%;
    background: var(--navy);
  }
  .contact__details {
    position: absolute; right: 36px; top: 34px;
    text-align: right;
  }
  .contact__brand {
    color: var(--navy);
    font-weight: 800; font-size: 30px;
    letter-spacing: 1px; text-transform: uppercase;
    margin-bottom: 22px;
  }
  .person-name {
    color: var(--navy); font-weight: 700; font-size: 21px; line-height: 1.1;
  }
  .person-title {
    color: var(--red); font-size: 13.5px; margin-bottom: 8px;
  }
  .service-area {
    color: var(--grey); font-size: 14px; line-height: 1.35;
    margin-bottom: 14px;
  }
  .contact-list { list-style: none; }
  .contact-list li {
    display: flex; justify-content: flex-end; align-items: center; gap: 8px;
    color: var(--grey); font-size: 14px; line-height: 1.5;
  }
  .contact-list svg { width: 13px; height: 13px; flex: none; }
</style>
</head>
<body>
<main class="canvas">

  <section class="card card--front">
    <div class="front__brand">
      <span class="brand-dot"></span>
      <span class="brand-name">Lantern Petro</span>
    </div>
    <div class="front__band">
      <p class="tagline">Lantern Petro, Powering the Nation's Oil &amp; Gas fields.</p>
      <p class="service-note">Frac fueling is what we do. We understand how important diesel fuel is to your operation, which is why our main service line is Frac fueling. We assure our supply and stand by our service</p>
    </div>
  </section>

  <section class="card card--contact">
    <div class="contact__mark" aria-hidden="true"></div>
    <div class="contact__details">
      <p class="contact__brand">Lantern Petro</p>
      <p class="person-name">Dale Winterholt</p>
      <p class="person-title">Owner/CEO</p>
      <p class="service-area">Servicing the Powder River<br>DJ basin &amp; Bakken formations.</p>
      <ul class="contact-list">
        <li>701.555.0148
          <svg viewBox="0 0 13 13" aria-label="Phone"><rect x="3" y="0.5" width="7" height="12" rx="1.3" fill="none" stroke="var(--navy)" stroke-width="1.4"/><circle cx="6.5" cy="10.3" r="0.8" fill="var(--navy)"/></svg>
        </li>
        <li>Dwinterholt@lanternpetro.com
          <svg viewBox="0 0 13 13" aria-label="Email"><rect x="0.5" y="2.5" width="12" height="8" fill="var(--navy)"/><path d="M0.8 2.8 L6.5 7.2 L12.2 2.8" fill="none" stroke="#fff" stroke-width="1"/></svg>
        </li>
        <li>www.Lanternpetro.com
          <svg viewBox="0 0 13 13" aria-label="Website"><circle cx="6.5" cy="6.5" r="6" fill="var(--navy)"/><ellipse cx="6.5" cy="6.5" rx="2.4" ry="6" fill="none" stroke="#fff" stroke-width="0.8"/><line x1="0.5" y1="6.5" x2="12.5" y2="6.5" stroke="#fff" stroke-width="0.8"/></svg>
        </li>
      </ul>
    </div>
  </section>

</main>
</body>
</html>
```